依頼詳細
表面は、
ロゴ
名前
会社名
本社の住所等で、(電話はいりません)

裏面には、3つの事業の情報をお願いします。
記載項目
添付いたします
希望イメージ
シンプル 複雑
単色 カラフル
暗い 明るい
日常 高級
遊び心 厳粛
未来的 伝統的
女性的 男性的
希望する色
赤系
納品ファイル
補足説明

```html
<!DOCTYPE html>
<html lang="ja">
<head>
<meta charset="utf-8">
<title>駿風学院 名刺</title>
<link href="https://fonts.googleapis.com/css2?family=Noto+Sans+JP:wght@400;500;700&family=Roboto+Mono:wght@400&display=swap" rel="stylesheet">
<style>
  :root {
    --paper: #ffffff;
    --brand: #8c1d40;
    --navy: #1e2b6e;
    --ink: #222222;
  }
  html, body {
    margin: 0;
    padding: 0;
    overflow: hidden;
    background: var(--paper);
  }
  .card {
    position: relative;
    width: 726px;
    height: 1200px;
    background: var(--paper);
    font-family: "Noto Sans JP", sans-serif;
    color: var(--ink);
    overflow: hidden;
  }
  .brand {
    position: absolute;
    top: 145px;
    left: 0;
    width: 100%;
    text-align: center;
  }
  .brand-dot {
    display: block;
    margin: 0 auto 110px;
    width: 130px;
    height: 130px;
  }
  .brand-name {
    margin: 0;
    font-size: 58px;
    font-weight: 500;
    letter-spacing: 4px;
    color: var(--brand);
    line-height: 1;
  }
  .person {
    position: absolute;
    top: 570px;
    left: 235px;
  }
  .person-role {
    margin: 0;
    font-size: 32px;
    font-weight: 400;
    letter-spacing: 3px;
    color: var(--ink);
  }
  .person-name {
    margin: 12px 0 0;
    font-size: 58px;
    font-weight: 700;
    letter-spacing: 8px;
    color: var(--navy);
    line-height: 1;
  }
  .person-roman {
    margin: 18px 0 0;
    font-size: 30px;
    font-weight: 400;
    letter-spacing: 1px;
    color: var(--ink);
  }
  .company {
    position: absolute;
    top: 946px;
    left: 235px;
    font-size: 30px;
    line-height: 38px;
    color: var(--ink);
  }
  .company-name {
    margin: 0 0 6px;
    font-size: 34px;
    font-weight: 700;
    line-height: 44px;
  }
  .company-name .corp {
    font-size: 28px;
    font-weight: 500;
  }
  .company-address {
    margin: 0;
    font-style: normal;
    font-weight: 500;
    letter-spacing: 2px;
  }
  .company-url {
    display: block;
    font-family: "Roboto Mono", monospace;
    font-size: 26px;
    letter-spacing: 1px;
    color: var(--ink);
    text-decoration: none;
  }
</style>
</head>
<body>
  <main class="card">
    <header class="brand">
      <svg class="brand-dot" viewBox="0 0 130 130" aria-hidden="true">
        <circle cx="65" cy="65" r="65" fill="var(--brand)"/>
      </svg>
      <p class="brand-name">駿風学院</p>
    </header>

    <section class="person">
      <p class="person-role">マネージャー</p>
      <h1 class="person-name">杉浦 朔</h1>
      <p class="person-roman">Sugiura Saku</p>
    </section>

    <footer class="company">
      <p class="company-name"><span class="corp">株式会社</span> 駿風学院</p>
      <address class="company-address">
        〒150-0042<br>
        東京都渋谷区宇田川町5番12号<br>
        宇田川テラスビルＣ棟４階
      </address>
      <a class="company-url" href="#">http://shunpu-gakuin.jp/</a>
    </footer>
  </main>
</body>
</html>
```